Rimo Application for Cars Accidents Services

We need app screen designs for company provide services for the cars that got accidents, the design should be modern official and simple, the pages around 26 include login, register, auth code, home, splash, request service, profile, settings, booking, booking info ..., we need something so professional please.

Target Market(s)

Cars owners

```html
<!DOCTYPE html>
<html lang="en">
<head>
<meta charset="utf-8">
<title>Rimo – App Screens</title>
<link href="https://fonts.googleapis.com/css2?family=Montserrat:wght@500;600;700;800&display=swap" rel="stylesheet">
<style>
:root{
  --bg:#8c8c8c;
  --white:#ffffff;
  --ink:#111318;
  --navy:#0f1420;
  --field:#eeeef0;
  --green-top:#3dbb3f;
  --green-bottom:#1e8f2a;
  --red-top:#f2182a;
  --red-bottom:#c90012;
  --accent-red:#e30613;
  --accent-green:#2aa53a;
  --line:#cfcfd4;
  --photo-a:#8f8a82;
  --photo-b:#3b3d42;
}
*{box-sizing:border-box;margin:0;padding:0}
html,body{width:702px;height:1200px;overflow:hidden}
body{background:var(--bg);font-family:'Montserrat',sans-serif;color:var(--ink);position:relative}
.screen{position:absolute;background:var(--white);overflow:hidden;box-shadow:0 6px 18px rgba(0,0,0,.25)}
.abs{position:absolute}
.brand{font-weight:800;color:var(--ink);letter-spacing:1px;display:flex;align-items:center;gap:6px}
.brand .dot{width:10px;height:10px;border-radius:50%;background:var(--accent-green)}
.brand.light{color:var(--white)}
.btn{position:absolute;display:flex;align-items:center;justify-content:center;gap:8px;color:var(--white);font-weight:700;border-radius:30px;letter-spacing:.3px}
.btn.green{background:linear-gradient(var(--green-top),var(--green-bottom))}
.btn.red{background:linear-gradient(var(--red-top),var(--red-bottom))}
.btn svg{width:14px;height:14px}
.field{position:absolute;background:var(--field);font-size:10px;font-weight:600;display:flex;align-items:center;padding-left:20px}
.title{position:absolute;font-weight:700;letter-spacing:.5px}

/* home */
.home{left:88px;top:73px;width:243px;height:526px;border-radius:22px}
.home .tour{left:0;width:100%;top:472px;text-align:center;font-size:16.5px;font-weight:600}

/* login */
.login{left:372px;top:89px;width:261px;height:495px}
.login .subtitle{left:13px;top:224px;font-size:20px;font-weight:500;color:#333}
.login .signup-note{left:0;width:100%;top:452px;text-align:center;font-size:11px;font-weight:500}
.login .signup-note span{color:var(--accent-red)}

/* register */
.register{left:88px;top:641px;width:261px;height:495px}

/* listing */
.listing{left:372px;top:614px;width:261px;height:529px}
.card{position:absolute;border:1px solid var(--line);background:var(--white)}
.card .name{font-weight:700;font-size:13px}
.card .price{font-size:9.5px;color:var(--accent-red)}
.card .class{font-size:9px;color:var(--accent-green)}
.car{position:absolute;border-radius:40% 45% 20% 20%/60% 60% 30% 30%}
</style>
</head>
<body>

<!-- Home -->
<section class="screen home">
  <div class="brand abs" style="left:0;width:100%;top:34px;justify-content:center;font-size:28px"><span class="dot"></span>RIMO</div>
  <svg class="abs" style="left:0;top:80px" width="243" height="215" viewBox="0 0 243 215" role="img" aria-label="Photo of a white service patrol car with checkered livery">
    <defs><linearGradient id="hp" x1="0" y1="0" x2="1" y2="1"><stop offset="0" stop-color="#8a7d70"/><stop offset=".6" stop-color="#d9dadc"/><stop offset="1" stop-color="#6e6f73"/></linearGradient></defs>
    <path d="M0 20 C40 -5 70 30 110 20 C150 8 180 -8 243 20 L243 195 C200 165 170 170 140 195 C110 218 70 210 40 195 C20 186 10 190 0 198 Z" fill="url(#hp)" stroke="var(--ink)" stroke-width="3"/>
  </svg>
  <div class="btn green" style="left:20px;top:318px;width:202px;height:58px;font-size:16px">ASK SERVICE <svg viewBox="0 0 16 16"><circle cx="8" cy="8" r="8" fill="#fff"/><path d="M6.5 4.5 10 8 6.5 11.5" stroke="var(--green-bottom)" stroke-width="2.2" fill="none"/></svg></div>
  <div class="btn red" style="left:20px;top:394px;width:202px;height:58px;font-size:16px">CAR RENTAL <svg viewBox="0 0 16 16"><circle cx="8" cy="8" r="8" fill="#fff"/><path d="M6.5 4.5 10 8 6.5 11.5" stroke="var(--red-bottom)" stroke-width="2.2" fill="none"/></svg></div>
  <div class="abs tour">Take tour to our Services</div>
</section>

<!-- Login -->
<section class="screen login">
  <svg class="abs" style="left:0;top:0" width="261" height="195" viewBox="0 0 261 195" role="img" aria-label="Photo of a smiling woman driving a car">
    <defs><linearGradient id="lp" x1="0" y1="0" x2="1" y2="1"><stop offset="0" stop-color="#e6e6e6"/><stop offset=".5" stop-color="#b9aa9c"/><stop offset="1" stop-color="#2a2b2f"/></linearGradient></defs>
    <path d="M50 0 C70 20 100 10 120 30 C150 55 140 110 170 140 C195 165 240 150 261 195 L261 0 Z" fill="url(#lp)" stroke="var(--ink)" stroke-width="3"/>
  </svg>
  <div class="brand abs" style="left:13px;top:64px;font-size:24px"><span class="dot"></span>RIMO</div>
  <div class="title" style="left:13px;top:181px;font-size:31px">CAR RENTAL</div>
  <div class="abs subtitle">Travel,Love a Car</div>
  <div class="field" style="left:13px;top:279px;width:231px;height:35px">Username *</div>
  <div class="field" style="left:13px;top:330px;width:231px;height:35px">Password *</div>
  <div class="btn green" style="left:13px;top:382px;width:231px;height:42px;font-size:16px">LOGIN ME <svg viewBox="0 0 16 16"><circle cx="8" cy="8" r="8" fill="#fff"/><path d="M6.5 4.5 10 8 6.5 11.5" stroke="var(--green-bottom)" stroke-width="2.2" fill="none"/></svg></div>
  <div class="abs signup-note">Don't have a Account? <span>Membership</span></div>
</section>

<!-- Register -->
<section class="screen register">
  <svg class="abs" style="left:0;top:0" width="261" height="190" viewBox="0 0 261 190" role="img" aria-label="Photo of a smiling man at the wheel of a car">
    <defs><linearGradient id="rp" x1="0" y1="0" x2="1" y2="1"><stop offset="0" stop-color="#9b8b7d"/><stop offset=".5" stop-color="#5d6068"/><stop offset="1" stop-color="#1e1f23"/></linearGradient></defs>
    <path d="M0 0 H261 V170 C235 150 210 155 185 175 C160 192 120 190 95 172 C70 152 35 150 0 170 Z" fill="url(#rp)" stroke="var(--ink)" stroke-width="3"/>
  </svg>
  <div class="brand abs" style="left:150px;top:34px;font-size:24px"><span class="dot"></span>RIMO</div>
  <div class="title" style="left:13px;top:212px;font-size:32px">SIGN UP</div>
  <div class="field" style="left:13px;top:272px;width:231px;height:35px">Phone</div>
  <div class="field" style="left:13px;top:322px;width:231px;height:35px">ID</div>
  <div class="field" style="left:13px;top:371px;width:231px;height:35px">Date of Birth</div>
  <div class="btn green" style="left:13px;top:422px;width:231px;height:42px;font-size:16px">SIGN UP <svg viewBox="0 0 16 16"><circle cx="8" cy="8" r="8" fill="#fff"/><path d="M6.5 4.5 10 8 6.5 11.5" stroke="var(--green-bottom)" stroke-width="2.2" fill="none"/></svg></div>
</section>

<!-- Listing -->
<section class="screen listing">
  <svg class="abs" style="left:0;top:0" width="261" height="90" viewBox="0 0 261 90">
    <path d="M0 0 H261 V80 C240 60 215 58 195 72 C170 90 100 92 70 70 C45 55 20 60 0 78 Z" fill="var(--navy)"/>
    <path d="M14 35 H26 M14 35 L18 31 M14 35 L18 39" stroke="#fff" stroke-width="2" fill="none"/>
    <circle cx="208" cy="33" r="5" stroke="#fff" stroke-width="2" fill="none"/><path d="M212 37 L216 41" stroke="#fff" stroke-width="2.4"/>
    <path d="M234 27 V43 M239 27 V43 M244 27 V43" stroke="#fff" stroke-width="1.6"/>
    <rect x="232" y="31" width="4" height="3" fill="#fff"/><rect x="237" y="37" width="4" height="3" fill="#fff"/><rect x="242" y="30" width="4" height="3" fill="#fff"/>
  </svg>
  <div class="brand light abs" style="left:0;width:100%;top:22px;justify-content:center;font-size:24px"><span class="dot"></span>RIMO</div>
  <div class="title" style="left:0;width:100%;text-align:center;top:110px;font-size:31px">SPORTS CAR</div>

  <div class="card" style="left:10px;top:164px;width:116px;height:89px;text-align:center">
    <div class="car" role="img" aria-label="Red sports car" style="left:27px;top:14px;width:64px;height:22px;background:linear-gradient(#f03a3a,#a80d0d)"></div>
    <div class="name abs" style="left:0;width:100%;top:49px">Sports Car</div>
    <div class="price abs" style="left:0;width:100%;top:67px">728/TEM</div>
  </div>
  <div class="card" style="left:134px;top:164px;width:116px;height:89px;text-align:center">
    <div class="car" role="img" aria-label="Silver sedan" style="left:22px;top:14px;width:72px;height:22px;background:linear-gradient(#d4d6da,#7b7f86)"></div>
    <div class="name abs" style="left:0;width:100%;top:49px">Supersports</div>
    <div class="price abs" style="left:0;width:100%;top:67px">38/TEM</div>
  </div>

  <div class="card" style="left:10px;top:261px;width:241px;height:76px">
    <div class="name abs" style="left:18px;top:11px">Meridian</div>
    <div class="class abs" style="left:18px;top:30px">Class $500</div>
    <div class="price abs" style="left:18px;top:50px">1 day /SR 480</div>
    <div class="car" role="img" aria-label="Red roadster" style="left:135px;top:14px;width:80px;height:26px;background:linear-gradient(#f03a3a,#a80d0d)"></div>
    <div class="abs" style="left:150px;width:52px;text-align:center;top:54px;font-size:11.5px;font-weight:500">Rentaro</div>
  </div>
  <div class="card" style="left:10px;top:345px;width:241px;height:76px">
    <div class="name abs" style="left:18px;top:11px">Meridian</div>
    <div class="class abs" style="left:18px;top:30px">Class $500</div>
    <div class="price abs" style="left:18px;top:50px">1 day /SR 480</div>
    <div class="car" role="img" aria-label="Dark grey roadster" style="left:135px;top:14px;width:80px;height:26px;background:linear-gradient(#6d7075,#25272b)"></div>
    <div class="abs" style="left:150px;width:52px;text-align:center;top:54px;font-size:11.5px;font-weight:500">Drivo</div>
  </div>
  <div class="card" style="left:10px;top:428px;width:241px;height:76px">
    <div class="name abs" style="left:18px;top:11px">Meridian</div>
    <div class="class abs" style="left:18px;top:30px">Class $500</div>
    <div class="price abs" style="left:18px;top:50px">1 day /SR 480</div>
    <div class="car" role="img" aria-label="Green roadster" style="left:135px;top:14px;width:80px;height:26px;background:linear-gradient(#3ed94a,#138a22)"></div>
    <div class="abs" style="left:150px;width:52px;text-align:center;top:54px;font-size:11.5px;font-weight:500">Wheelix</div>
  </div>
</section>

</body>
</html>
```